Business Card Design Project- Removalist

I would like to surprise my husband to be with a different type of wedding present. His brother (who he owned a removalist business with) suddenly passed away from cancer recently and he has changed his business name to 'RTB' (which stands for Raising Tom Bright; but the full name doesn't need to be on the business card as it is more of a personal business name). To celebrate the new business I would like to get him some business cards made.
I would like the business name to be listed as 'RTB' and somewhere on the card I would like 'Sydney wide removals and relocation services'. I would like it to be obvious from the front of the card that it is a removalist business card. If a truck or some other feature that makes it look like a removalist business card could added it would be appreciated.
I don't mind what colours are used, but I would like the colour blue to feature somewhere in the design. It can be bright and fun, which is how Tom was.
I will also need the company's email address and phone number listed
The email address is: rtbremovals@quillpost.example
The contact number is: 0417 282 934
I don't need a contact name listed on the card, but perhaps 'Owned and operated by the Pendleworth family' could be added near the contact details in small font.
Thank you very much for considering this project!
Kind regards,
Fiona
Updates
Could you please change the mobile contact number to 0417 282 934. This is the only contact phone number required on the card now.
Thank you!

```html
<!DOCTYPE html>
<html lang="en">
<head>
<meta charset="utf-8">
<title>RTB Business Card – Front and Back</title>
<link rel="stylesheet" href="https://fonts.googleapis.com/css2?family=Source+Sans+3:wght@400;600&display=swap">
<style>
  :root {
    --page-bg: #dcdcdc;
    --card-white: #ffffff;
    --card-warm: #ecebe6;
    --cyan: #0fa4cf;
    --cyan-pale: #bfe6f1;
    --teal: #0a9aa0;
    --ink: #111111;
    --ghost: #b8b8b8;
    --truck-teal: #1f8a93;
    --truck-dark: #2f3a3d;
  }
  html, body {
    margin: 0;
    padding: 0;
    width: 786px;
    height: 1200px;
    overflow: hidden;
    background: var(--page-bg);
  }
  .canvas {
    position: relative;
    width: 786px;
    height: 1200px;
  }
  .business-card {
    position: absolute;
    width: 544px;
    height: 358px;
    display: block;
  }
  .business-card--front { left: 121px; top: 114px; }
  .business-card--back  { left: 139px; top: 689px; }

  .card-font { font-family: "Source Sans 3", "Myriad Pro", sans-serif; }
  .brand-name { font-size: 52px; font-weight: 400; fill: var(--ink); }
  .brand-ghost { font-size: 128px; font-weight: 400; fill: var(--ghost); opacity: 0.75; }
  .tagline { font-size: 15px; fill: var(--card-white); }
  .contact-line { font-size: 13.5px; fill: var(--ink); }
  .speed-line { fill: var(--cyan-pale); }
  .truck-placeholder { fill: url(#truckFill); }

  .stop-white { stop-color: var(--card-white); }
  .stop-warm { stop-color: var(--card-warm); }
  .stop-cyan { stop-color: var(--cyan); }
  .stop-cyan-pale { stop-color: var(--cyan-pale); }
  .stop-teal { stop-color: var(--teal); }
  .stop-truck { stop-color: var(--truck-teal); }
  .stop-truck-dark { stop-color: var(--truck-dark); }
</style>
</head>
<body>
<main class="canvas">

  <!-- Front of card -->
  <svg class="business-card business-card--front card-font" viewBox="0 0 544 358" xmlns="http://www.w3.org/2000/svg">
    <defs>
      <linearGradient id="paperFront" x1="0" y1="0" x2="1" y2="0.4">
        <stop offset="0" class="stop-white"/>
        <stop offset="1" class="stop-warm"/>
      </linearGradient>
      <linearGradient id="barFadeIn" x1="0" y1="0" x2="1" y2="0">
        <stop offset="0" class="stop-white"/>
        <stop offset="1" class="stop-cyan-pale"/>
      </linearGradient>
      <linearGradient id="barSolid" x1="0" y1="0" x2="1" y2="0">
        <stop offset="0" class="stop-cyan"/>
        <stop offset="1" class="stop-cyan"/>
      </linearGradient>
      <linearGradient id="stripeBand" x1="0" y1="0" x2="1" y2="0">
        <stop offset="0" class="stop-cyan"/>
        <stop offset="0.6" class="stop-cyan"/>
        <stop offset="1" class="stop-cyan-pale"/>
      </linearGradient>
      <linearGradient id="footerWash" x1="0" y1="1" x2="1" y2="0">
        <stop offset="0" class="stop-white"/>
        <stop offset="0.35" class="stop-cyan"/>
        <stop offset="1" class="stop-teal"/>
      </linearGradient>
      <linearGradient id="truckFill" x1="0" y1="0" x2="0" y2="1">
        <stop offset="0" class="stop-truck"/>
        <stop offset="1" class="stop-truck-dark"/>
      </linearGradient>
    </defs>

    <rect class="card-paper" width="544" height="358" fill="url(#paperFront)"/>

    <g class="header-bars">
      <rect x="0" y="48" width="247" height="43" fill="url(#barFadeIn)"/>
      <rect x="394" y="48" width="150" height="43" fill="url(#barSolid)"/>
    </g>
    <text class="brand-name" x="255" y="86">RTB</text>

    <text class="brand-ghost" x="133" y="222">RTB</text>

    <g class="speed-lines">
      <rect class="speed-line" x="5" y="169" width="237" height="4"/>
      <rect class="speed-line" x="5" y="180" width="237" height="4"/>
      <rect class="speed-line" x="5" y="191" width="237" height="4"/>
      <rect class="speed-line" x="5" y="202" width="237" height="4"/>
      <rect class="speed-line" x="5" y="213" width="237" height="4"/>
      <rect class="speed-line" x="5" y="224" width="237" height="4"/>
    </g>

    <rect class="truck-placeholder" x="255" y="172" width="191" height="73" rx="6"
          role="img" aria-label="Teal pickup truck driving to the right"/>

    <rect class="stripe-band" x="0" y="245" width="544" height="30" fill="url(#stripeBand)"/>
    <rect class="footer-wash" x="0" y="275" width="544" height="83" fill="url(#footerWash)"/>

    <text class="tagline" x="300" y="309" text-anchor="middle">Sydney wide removals and relocation services</text>
  </svg>

  <!-- Back of card -->
  <svg class="business-card business-card--back card-font" viewBox="0 0 544 358" xmlns="http://www.w3.org/2000/svg">
    <defs>
      <linearGradient id="paperBack" x1="0" y1="0" x2="1" y2="0.4">
        <stop offset="0" class="stop-white"/>
        <stop offset="1" class="stop-warm"/>
      </linearGradient>
      <linearGradient id="barFadeInBack" x1="0" y1="0" x2="1" y2="0">
        <stop offset="0" class="stop-white"/>
        <stop offset="1" class="stop-cyan-pale"/>
      </linearGradient>
      <linearGradient id="barRightBack" x1="0" y1="0" x2="1" y2="0">
        <stop offset="0" class="stop-cyan-pale"/>
        <stop offset="1" class="stop-cyan"/>
      </linearGradient>
      <linearGradient id="stripeBandBack" x1="0" y1="0" x2="1" y2="0">
        <stop offset="0" class="stop-cyan"/>
        <stop offset="0.6" class="stop-cyan"/>
        <stop offset="1" class="stop-cyan-pale"/>
      </linearGradient>
      <linearGradient id="footerWashBack" x1="0" y1="1" x2="1" y2="0">
        <stop offset="0" class="stop-white"/>
        <stop offset="0.35" class="stop-cyan"/>
        <stop offset="1" class="stop-teal"/>
      </linearGradient>
    </defs>

    <rect class="card-paper" width="544" height="358" fill="url(#paperBack)"/>

    <g class="header-bars">
      <rect x="0" y="48" width="244" height="43" fill="url(#barFadeInBack)"/>
      <rect x="394" y="48" width="150" height="43" fill="url(#barRightBack)"/>
    </g>
    <text class="brand-name" x="257" y="86">RTB</text>

    <g class="contact-details">
      <text class="contact-line" x="154" y="134">Owned and operated by the Pendleworth family</text>
      <text class="contact-line" x="154" y="150">Email address: rtbremovals@quillpost.example</text>
      <text class="contact-line" x="154" y="166">contact number: 0417 282 934</text>
    </g>

    <rect class="stripe-band" x="0" y="244" width="544" height="31" fill="url(#stripeBandBack)"/>
    <rect class="footer-wash" x="0" y="275" width="544" height="83" fill="url(#footerWashBack)"/>
  </svg>

</main>
</body>
</html>
```